Boutique custom software development company needs new business card

Our nearly 20 year old custom software development company would like to better include the fact that we are now providing Bitcoin services. These new services are B2B include education (how to acquire and securely hold Bitcoin) and integrating Bitcoin payments into existing ecommerce sites or other existing systems. Please keep the card clean and simple. Attached is our current design and some other files. vexalon.example

Target Market(s)

businesses owners interested in long term relationship

Industry/Entity Type

Custom software development and Bitcoin

Contact Information for Business Card

Marcus Ellwood, marcus@vexalon.example, vexalon.example, (888) 555-VEXAL

Font styles to use
Other font styles liked:
• monospace

Requirements
Must have
• double-sided
Nice to have
• clean and simple
Should not have
• physical address

```html
<!DOCTYPE html>
<html lang="en">
<head>
<meta charset="utf-8">
<title>Vexalon Business Card</title>
<link rel="stylesheet" href="https://fonts.googleapis.com/css2?family=Open+Sans:wght@400;600;700&display=swap">
<style>
  :root {
    --page: #ffffff;
    --card: #e2e8f0;
    --brand-blue: #3b73b9;
    --brand-orange: #f07c22;
    --ink: #111111;
  }
  * { margin: 0; padding: 0; box-sizing: border-box; }
  html, body {
    width: 1200px; height: 1200px; overflow: hidden;
    background: var(--page);
    font-family: "Open Sans", Arial, sans-serif;
  }
  .canvas { position: relative; width: 1200px; height: 1200px; }
  .card {
    position: absolute; left: 102px; width: 995px; height: 569px;
    background: var(--card);
  }
  .card--front { top: 12px; }
  .card--back { top: 613px; }
  .centered { position: absolute; left: 0; right: 0; text-align: center; white-space: nowrap; }

  .wordmark {
    top: 318px; font-size: 112px; font-weight: 700; line-height: 1;
    color: var(--brand-blue); letter-spacing: 0;
  }
  .tagline-row {
    position: absolute; left: 0; right: 0; top: 450px;
    display: flex; justify-content: center; align-items: center; gap: 14px;
  }
  .tagline { font-size: 30px; font-weight: 400; color: var(--brand-blue); line-height: 1.2; white-space: nowrap; }
  .tagline-rule { width: 40px; height: 3px; background: var(--brand-orange); margin-top: 22px; }

  .brand-square {
    position: absolute; left: 392px; top: 63px; width: 212px; height: 201px;
    background: var(--brand-blue);
  }
  .web-address { top: 268px; font-size: 34px; color: var(--brand-orange); line-height: 1.1; }
  .divider {
    position: absolute; left: 184px; top: 319px; width: 626px; height: 3px; background: var(--brand-blue);
  }
  .contact-name { top: 337px; font-size: 34px; font-weight: 700; color: var(--brand-blue); letter-spacing: -1px; line-height: 1.1; }
  .contact-phone { top: 376px; font-size: 31px; color: var(--brand-orange); line-height: 1.1; }
  .contact-email { top: 431px; font-size: 33px; color: var(--brand-blue); line-height: 1.1; }
  .services { top: 479px; font-size: 29px; color: var(--ink); line-height: 1.1; }
</style>
</head>
<body>
<div class="canvas">
  <section class="card card--front">
    <div class="centered wordmark">VEXALON</div>
    <div class="tagline-row">
      <span class="tagline-rule"></span>
      <span class="tagline">Website &amp; Application Development</span>
      <span class="tagline-rule"></span>
    </div>
  </section>

  <section class="card card--back">
    <div class="brand-square"></div>
    <div class="centered web-address">vexalon.example</div>
    <div class="divider"></div>
    <div class="centered contact-name">Marcus Ellwood</div>
    <div class="centered contact-phone">(888) 555-VEXAL</div>
    <div class="centered contact-email">Marcus Ellwood, marcus@vexalon.example</div>
    <div class="centered services">Bitcoin Education &amp; Payment Integration</div>
  </section>
</div>
</body>
</html>
```